Test and Tag business card design

We are an appliance test and tag company in Brisbane Australia requiring a business card design.
I don't have a logo.
Card front: Matte black background with white font.
Card back: White background with black font colour
Examples are attached
Minimalist design
Reason: Looking for more designs with an extreme minimal feel
Industry/Entity Type
Appliance
Contact Information for Business Card
Business name: Summit Check and Label
Description: Onsite Electrical Testing and Tagging
Licence No. 48213
Name: Greg Palmby
Mobile: 0417 592 348
Email: greg@summitcheckandlabel.com.au
Web: summitcheckandlabel.com.au
Logo Text
Summit Check and Label
Look and feel

```html
<!DOCTYPE html>
<html lang="en">
<head>
<meta charset="utf-8">
<title>Summit Check and Label – Business Card</title>
<link rel="stylesheet" href="https://fonts.googleapis.com/css2?family=Open+Sans:wght@400;600;700&display=swap">
<style>
  :root {
    --bg: #d9d9d9;
    --paper: #f3f3f3;
    --ink: #2f2f2f;
    --matte: #1e1e1e;
    --matte-low: #222222;
    --white: #f2f2f2;
    --soft-text: #d8d8d8;
    --green: #7ab51d;
    --green-dark: #5f9312;
    --stripe: #b9b9b9;
    --stripe-light: #e6e6e6;
  }
  * { margin: 0; padding: 0; box-sizing: border-box; }
  html, body {
    width: 1200px; height: 1152px; overflow: hidden;
    background: var(--bg);
    font-family: "Open Sans", Arial, sans-serif;
  }
  .card {
    position: absolute; left: 130px; width: 940px; height: 520px;
    overflow: hidden;
    box-shadow: 0 10px 30px rgba(0,0,0,0.25);
  }
  .card--back { top: 40px; background: linear-gradient(160deg, #fafafa, #e9e9e9); }
  .card--front { top: 592px; background: var(--matte); }

  .stripe {
    position: absolute; left: 0; right: 0; height: 16px;
    background: linear-gradient(var(--stripe-light) 0 40%, var(--stripe) 40% 100%);
  }
  .band {
    position: absolute; left: 0; right: 0; bottom: 0;
    background: linear-gradient(180deg, var(--green), var(--green-dark));
  }
  .card--back .stripe { bottom: 70px; }
  .card--back .band { height: 70px; }

  .back-brand {
    position: absolute; left: 0; right: 0; top: 180px; text-align: center; color: var(--ink);
  }
  .back-brand__name { font-weight: 700; font-size: 54px; letter-spacing: -1px; line-height: 1; }
  .back-brand__web { margin-top: 12px; font-size: 24px; letter-spacing: 2px; }

  .front-person {
    position: absolute; right: 70px; top: 50px;
    color: var(--white); font-weight: 700; font-size: 40px;
  }
  .front-brand {
    position: absolute; left: 80px; top: 210px;
    color: var(--white); font-weight: 700; font-size: 54px; letter-spacing: -1px;
  }
  .front-contact {
    position: absolute; left: 0; right: 0; top: 310px; height: 124px;
    background: var(--matte-low); border-top: 1px solid #2a2a2a;
  }
  .contact-item {
    position: absolute; display: flex; align-items: center; gap: 14px;
    color: var(--soft-text); font-size: 21px; letter-spacing: 0.5px;
  }
  .contact-item svg { width: 22px; height: 22px; flex: none; }
  .contact-item--phone { left: 210px; top: 62px; }
  .contact-item--web { left: 520px; top: 28px; }
  .contact-item--mail { left: 520px; top: 70px; }
  .card--front .stripe { bottom: 70px; }
  .card--front .band {
    height: 70px; display: flex; align-items: center; justify-content: center;
    color: #262626; font-weight: 700; font-size: 28px; letter-spacing: -0.3px;
  }
</style>
</head>
<body>
  <section class="card card--back">
    <div class="back-brand">
      <div class="back-brand__name">SUMMIT CHECK AND LABEL</div>
      <div class="back-brand__web">www.summitcheckandlabel.com.au</div>
    </div>
    <div class="stripe"></div>
    <div class="band"></div>
  </section>

  <section class="card card--front">
    <div class="front-person">GREG PALMBY</div>
    <div class="front-brand">SUMMIT CHECK AND LABEL</div>
    <div class="front-contact">
      <div class="contact-item contact-item--phone">
        <svg viewBox="0 0 24 24" aria-hidden="true"><path d="M7 3c2 0 3 3 3 4s-2 2-2 3c1 3 3 5 6 6 1 0 2-2 3-2s4 1 4 3-2 4-4 4C9 21 3 15 3 7c0-2 2-4 4-4z" fill="#7ab51d"/></svg>
        <span>0417 592 348</span>
      </div>
      <div class="contact-item contact-item--web">
        <svg viewBox="0 0 24 24" aria-hidden="true"><circle cx="12" cy="12" r="10" fill="#7ab51d"/><path d="M2 12h20M12 2c3 3 3 17 0 20M12 2c-3 3-3 17 0 20" stroke="#1e1e1e" stroke-width="1.5" fill="none"/></svg>
        <span>www.summitcheckandlabel.com.au</span>
      </div>
      <div class="contact-item contact-item--mail">
        <svg viewBox="0 0 24 24" aria-hidden="true"><rect x="2" y="5" width="20" height="14" fill="none" stroke="#7ab51d" stroke-width="2"/><path d="M2 5l10 8 10-8" fill="none" stroke="#7ab51d" stroke-width="2"/></svg>
        <span>greg@summitcheckandlabel.com.au</span>
      </div>
    </div>
    <div class="stripe"></div>
    <div class="band">ONSITE ELECTRICAL TESTING AND TAGGING - LICENSE NO. 48213</div>
  </section>
</body>
</html>
```